Business Card Design

we sell natural, organic & biological products. our brand includes verdalune - hair dye products, morvesa-baby skin care and toothpaste... all products from Italy. our target customers are pharmacies, organic shops & stores, mum and baby care shops,.. i would love to see designs that use natural color, simple, friendly, eco concept.
Il Campo Vesco is Italian language, means Quiet meadow, referring to the best parts on the top of wheat. The brands we carried currently are VerdaLune Piana and Morvesa.

Target Market(s)

organic shops & store, pharmacies, mum n baby shops, bio/organic product users

Industry/Entity Type

Hair

Contact Information for Business Card

Mabel Khoo WeiTing
Sales Manager
Il Campo Vesco Singapore
Blk 318 Pinecrest Avenue7
#07-12 Singapore 648271
Tel +65 6173 4820 Mobile +65 87460395
Reg No 48207315K
www.facebook.com/ilcampovescosg

Requirements
Must have
• The front of the card should have my name, followed by my job title, my email address. Then the office address (company reg no), office tel, mobile phone.

My namecard should have all the brands my company carries.
Like ‘Morvesa’, ‘Verdalune piana’. Should have the brand logos too. This should be stated clearly at the back of the card. I will upload 'Verdalune' logo once I have it.

```html
<!DOCTYPE html>
<html lang="en">
<head>
<meta charset="utf-8">
<title>Il Campo Vesco – Business Card</title>
<link rel="stylesheet" href="https://fonts.googleapis.com/css2?family=Oswald:wght@500&family=Roboto:wght@300;400&display=swap">
<style>
  :root {
    --stage: #d6d6d6;
    --card: #fbfbfb;
    --brand-blue: #1ba1dd;
    --leaf-green: #7ac143;
    --name-red: #c8102e;
    --ink: #2f2f2f;
    --ink-soft: #555555;
    --rule: #e2e2e2;
  }
  html, body {
    margin: 0;
    width: 1200px;
    height: 947px;
    overflow: hidden;
  }
  body {
    background: radial-gradient(ellipse at center, #e6e6e6 0%, var(--stage) 75%);
    font-family: "Roboto", sans-serif;
    position: relative;
  }
  .card {
    position: absolute;
    top: 150px;
    width: 380px;
    height: 640px;
    background: var(--card);
    border-radius: 26px;
    box-shadow: 0 10px 30px rgba(0,0,0,0.18);
    box-sizing: border-box;
  }
  .card--back { left: 170px; }
  .card--front { left: 650px; }

  .brand {
    display: flex;
    flex-direction: column;
    align-items: center;
    gap: 10px;
  }
  .brand__dot {
    width: 34px;
    height: 34px;
    border-radius: 50%;
    background: var(--leaf-green);
  }
  .brand__name {
    font-weight: 400;
    font-size: 26px;
    letter-spacing: 2px;
    color: var(--brand-blue);
    white-space: nowrap;
  }
  .card--back .brand {
    position: absolute;
    left: 0; right: 0;
    top: 250px;
  }

  .carried {
    position: absolute;
    left: 40px; right: 40px;
    top: 430px;
    border-top: 1px solid var(--rule);
    padding-top: 18px;
    text-align: center;
  }
  .carried__title {
    font-size: 12px;
    letter-spacing: 2px;
    color: var(--ink-soft);
    text-transform: uppercase;
  }
  .carried__list {
    display: flex;
    justify-content: center;
    gap: 28px;
    margin-top: 14px;
  }
  .carried__item {
    display: flex;
    align-items: center;
    gap: 7px;
    font-size: 16px;
    color: var(--ink);
    white-space: nowrap;
  }
  .carried__mark {
    width: 12px;
    height: 12px;
    border-radius: 50%;
    background: var(--leaf-green);
  }

  .social {
    position: absolute;
    right: 30px;
    bottom: 28px;
    display: flex;
    gap: 16px;
  }
  .social__item {
    display: flex;
    align-items: center;
    gap: 5px;
    font-size: 11px;
    color: var(--ink-soft);
  }
  .social__mark {
    width: 16px;
    height: 16px;
    background: var(--leaf-green);
    border-radius: 2px;
  }

  .card--front .brand { margin-top: 60px; }
  .contact {
    margin: 36px 0 0 48px;
    display: flex;
    flex-direction: column;
    gap: 30px;
  }
  .contact__row {
    display: flex;
    align-items: center;
    gap: 14px;
  }
  .contact__icon {
    width: 34px;
    height: 34px;
    flex: none;
  }
  .contact__bar {
    width: 4px;
    align-self: stretch;
    min-height: 40px;
    background: var(--ink);
    flex: none;
  }
  .contact__text {
    font-size: 15px;
    line-height: 1.4;
    color: var(--ink);
    font-weight: 300;
  }
  .person__name {
    font-family: "Oswald", sans-serif;
    font-size: 27px;
    line-height: 1;
    letter-spacing: 0.5px;
    color: var(--ink);
    font-weight: 500;
  }
  .person__first { color: var(--name-red); }
  .person__role {
    font-size: 13px;
    color: var(--ink-soft);
    margin-top: 4px;
  }
</style>
</head>
<body>

  <section class="card card--back" aria-label="Card back">
    <div class="brand">
      <span class="brand__dot"></span>
      <span class="brand__name">IL CAMPO VESCO</span>
    </div>

    <div class="carried">
      <div class="carried__title">Our brands</div>
      <div class="carried__list">
        <span class="carried__item"><span class="carried__mark"></span>Morvesa</span>
        <span class="carried__item"><span class="carried__mark"></span>VerdaLune Piana</span>
      </div>
    </div>

    <div class="social">
      <span class="social__item"><span class="social__mark"></span>feedlink</span>
      <span class="social__item"><span class="social__mark"></span>chatter</span>
    </div>
  </section>

  <section class="card card--front" aria-label="Card front">
    <div class="brand">
      <span class="brand__dot"></span>
      <span class="brand__name">IL CAMPO VESCO</span>
    </div>

    <div class="contact">
      <div class="contact__row">
        <svg class="contact__icon" viewBox="0 0 34 34" aria-hidden="true">
          <circle cx="17" cy="10" r="7" fill="var(--brand-blue)"/>
          <path d="M3 33c0-9 6-14 14-14s14 5 14 14z" fill="var(--brand-blue)"/>
        </svg>
        <span class="contact__bar"></span>
        <div class="contact__text">
          <div class="person__name"><span class="person__first">HENRY</span> MARLOWE</div>
          <div class="person__role">Managing Director</div>
        </div>
      </div>

      <div class="contact__row">
        <svg class="contact__icon" viewBox="0 0 34 34" aria-hidden="true">
          <path d="M17 2a11 11 0 0 0-11 11c0 8 11 19 11 19s11-11 11-19A11 11 0 0 0 17 2z" fill="var(--brand-blue)"/>
          <circle cx="17" cy="13" r="4.5" fill="var(--card)"/>
        </svg>
        <span class="contact__bar"></span>
        <div class="contact__text">
          417 9th floor Arcade<br>Fenmore Road QTR<br>Reg No 48207315K
        </div>
      </div>

      <div class="contact__row">
        <svg class="contact__icon" viewBox="0 0 34 34" aria-hidden="true">
          <circle cx="17" cy="17" r="15" fill="var(--brand-blue)"/>
          <g fill="none" stroke="var(--card)" stroke-width="1.6">
            <ellipse cx="17" cy="17" rx="6.5" ry="15"/>
            <line x1="17" y1="2" x2="17" y2="32"/>
            <line x1="2" y1="17" x2="32" y2="17"/>
            <path d="M5 9.5h24M5 24.5h24"/>
          </g>
        </svg>
        <span class="contact__bar"></span>
        <div class="contact__text">
          Tel 014 738 2605<br>Mobile +65 87460395<br>henry@campomail.com<br>campovescoshop.com
        </div>
      </div>
    </div>
  </section>

</body>
</html>
```